We are wanting a designer to design an ebook on Residential Property in Australia. This ebook is a quarterly report and covers 5 major capital cities in Australia. This is the first quarterly report for the year - another 3 are needed to be created. If you are chosen as our designer please expect ongoing work which is well rewarded.

To begin with:

We will only need you to design a few pages so we can see your style. Then if you are chosen we will get you to do the whole thing.

Can you please design the title page, page 5 and the Adelaide section(page 6 & 7) of the The Suburban Dwelling Forecast - Seasonal Capital Briefing - Q1 2014 document attached.

The ebook brief:

You will need to create 2 graphs to include in the ebook from the data I give to you for each capital city (one graph for houses and one graph for units).

We already have a style of ebook in mind from a previous ebook our in-office designer has created for our company. You will need to keep with the logo/style/colours/fonts etc. We are looking for a designer based in Australia.

Sources and content:

Below I have shared a dropbox folder with you. It contains the first ebook our designer has created for you to view the style,logo etc - YieldHaven-Property-ebook. The folder also contains the source files for the logo.

https://www.filecrate-share.com/sh/k4p2xq7vb9rm3d/BXQ581zt/

The Suburban Dwelling Forecast - Seasonal Capital Briefing - Q1 2014 document attached is the content we need made into the ebook.

Each page has been set out with the content needed for that page. Each capital city content spreads out over two pages with a graph on each. I have highlighted in red the data needed to create each of the graphs. The graph style must look like the Sector Horizon image in the shared dropbox folder.

You will also need to redesign the graph on page 5. You may do this how you like as long as it keeps in the style of the ebook. We will also need the source files on this ebook.

```html
<!DOCTYPE html>
<html lang="en">
<head>
<meta charset="utf-8">
<title>Positive growth – Page 6</title>
<link href="https://fonts.googleapis.com/css2?family=Lato:wght@400;700;900&display=swap" rel="stylesheet">
<style>
  :root {
    --accent-red: #b0252a;
    --body-text: #3a3a3c;
    --panel-grey: #d5d6d8;
    --tab-grey: #58595b;
    --rule-dark: #4a4b4d;
    --house-navy: #353f7a;
    --unit-teal: #0f5546;
    --grid-line: #b9babc;
    --sky-top: #3d6fb0;
    --sky-mid: #8fb0d6;
    --city-warm: #b98a55;
    --city-shadow: #3b3a34;
  }
  * { margin: 0; padding: 0; box-sizing: border-box; }
  html, body { width: 849px; height: 1200px; overflow: hidden; background: #fff; }
  body { font-family: "Lato", Arial, sans-serif; color: var(--body-text); position: relative; }

  .hero-photo {
    position: absolute; left: 0; top: 0; width: 849px; height: 565px;
    background: linear-gradient(180deg, var(--sky-top) 0%, var(--sky-mid) 28%, var(--city-warm) 55%, var(--city-shadow) 100%);
  }

  .section-title {
    position: absolute; left: 44px; top: 610px;
    font-size: 27px; font-weight: 900; color: var(--accent-red);
  }
  .article { position: absolute; left: 44px; top: 660px; width: 762px; font-size: 15px; line-height: 18px; }
  .article h3 { font-size: 15px; font-weight: 700; }
  .article p { margin-bottom: 18px; }

  .chart-panel {
    position: absolute; left: 44px; top: 887px; width: 761px; height: 268px;
    background: var(--panel-grey); border-top: 2px solid var(--rule-dark);
  }
  .chart-tab {
    position: absolute; left: 228px; top: 873px; width: 393px; height: 28px;
    background: var(--tab-grey); color: #fff; font-size: 14px;
    display: flex; align-items: center; justify-content: center;
  }
  .chart-svg { position: absolute; left: 44px; top: 887px; }
  .axis-label { font-size: 11px; fill: #333; text-anchor: end; }
  .city-label { font-size: 11.5px; fill: #333; text-anchor: middle; }
  .bar-value { font-size: 11.5px; fill: #fff; }
  .legend-label { font-size: 12px; fill: #333; }

  .page-number { position: absolute; right: 44px; top: 1170px; font-size: 12px; }
  .page-number strong { font-weight: 900; }
</style>
</head>
<body>
  <div class="hero-photo" role="img" aria-label="Aerial view of city office towers and an elevated freeway under a cloudy evening sky"></div>

  <h2 class="section-title">Positive growth</h2>

  <div class="article">
    <h3>More million dollar suburbs than ever before</h3>
    <p>A positive indicator of a strong property market is the number of suburbs which record a million dollar median price range. This is becoming a common feature in property markets across most Australian capital cities.</p>
    <p>According to recent statistics from Propdex, the residential property market is booming with million dollar suburbs. Australia currently has 279 suburbs where the house price median is one million or more, and 23 suburbs where the average unit price is one million or above.</p>
    <p>In the housing market, Sydney currently leads the nation with 181 recorded million dollar suburbs. This is followed by Melbourne with 51, Perth with 43, Brisbane with 13, and Adelaide with 8. (Source: Propdex)</p>
  </div>

  <div class="chart-panel"></div>
  <svg class="chart-svg" width="761" height="268" viewBox="44 887 761 268">
    <g stroke="var(--grid-line)" stroke-width="1">
      <line x1="175" y1="918.8" x2="645" y2="918.8"/>
      <line x1="175" y1="945.2" x2="645" y2="945.2"/>
      <line x1="175" y1="971.6" x2="645" y2="971.6"/>
      <line x1="175" y1="998" x2="645" y2="998"/>
      <line x1="175" y1="1024.4" x2="645" y2="1024.4"/>
      <line x1="175" y1="1050.8" x2="645" y2="1050.8"/>
      <line x1="175" y1="1077.2" x2="645" y2="1077.2"/>
      <line x1="175" y1="1103.6" x2="645" y2="1103.6"/>
      <line x1="175" y1="1130" x2="645" y2="1130"/>
    </g>
    <g class="axis-label">
      <text x="168" y="922.8">$800,000</text>
      <text x="168" y="949.2">$700,000</text>
      <text x="168" y="975.6">$600,000</text>
      <text x="168" y="1002">$500,000</text>
      <text x="168" y="1028.4">$400,000</text>
      <text x="168" y="1054.8">$300,000</text>
      <text x="168" y="1081.2">$200,000</text>
      <text x="168" y="1107.6">$100,000</text>
    </g>

    <g fill="var(--house-navy)">
      <rect x="188" y="1022.4" width="24" height="107.6"/>
      <rect x="246" y="1009.5" width="24" height="120.5"/>
      <rect x="304" y="969" width="24" height="161"/>
      <rect x="363" y="991.5" width="24" height="138.5"/>
      <rect x="421" y="926.5" width="24" height="203.5"/>
      <rect x="480" y="991.3" width="24" height="138.7"/>
      <rect x="538" y="977.8" width="24" height="152.2"/>
      <rect x="597" y="1030.9" width="24" height="99.1"/>
    </g>
    <g fill="var(--unit-teal)">
      <rect x="217" y="1049.5" width="24" height="80.5"/>
      <rect x="275" y="1036.3" width="24" height="93.7"/>
      <rect x="333" y="1011.3" width="24" height="118.7"/>
      <rect x="392" y="1010" width="24" height="120"/>
      <rect x="450" y="988.2" width="24" height="141.8"/>
      <rect x="509" y="1022.2" width="24" height="107.8"/>
      <rect x="567" y="1016.2" width="24" height="113.8"/>
      <rect x="626" y="1062" width="24" height="68"/>
    </g>

    <g class="bar-value">
      <text transform="translate(204 1126) rotate(-90)">407,500</text>
      <text transform="translate(233 1126) rotate(-90)">305,000</text>
      <text transform="translate(262 1126) rotate(-90)">456,500</text>
      <text transform="translate(291 1126) rotate(-90)">355,000</text>
      <text transform="translate(320 1126) rotate(-90)">610,000</text>
      <text transform="translate(349 1126) rotate(-90)">449,500</text>
      <text transform="translate(379 1126) rotate(-90)">524,500</text>
      <text transform="translate(408 1126) rotate(-90)">454,500</text>
      <text transform="translate(437 1126) rotate(-90)">771,000</text>
      <text transform="translate(466 1126) rotate(-90)">537,000</text>
      <text transform="translate(496 1126) rotate(-90)">525,500</text>
      <text transform="translate(525 1126) rotate(-90)">408,500</text>
      <text transform="translate(554 1126) rotate(-90)">576,500</text>
      <text transform="translate(583 1126) rotate(-90)">431,000</text>
      <text transform="translate(613 1126) rotate(-90)">375,500</text>
      <text transform="translate(642 1126) rotate(-90)">257,500</text>
    </g>

    <g class="city-label">
      <text x="214" y="1144">Adelaide</text>
      <text x="272" y="1144">Brisbane</text>
      <text x="330" y="1144">Melbourne</text>
      <text x="389" y="1144">Perth</text>
      <text x="447" y="1144">Sydney</text>
      <text x="506" y="1144">Canberra</text>
      <text x="564" y="1144">Darwin</text>
      <text x="623" y="1144">Hobart</text>
    </g>

    <rect x="667" y="997" width="18" height="18" fill="var(--house-navy)"/>
    <rect x="667" y="1018" width="18" height="18" fill="var(--unit-teal)"/>
    <text class="legend-label" x="692" y="1010">Houses</text>
    <text class="legend-label" x="692" y="1031">Units</text>
  </svg>

  <div class="page-number"><strong>6</strong> | Page</div>
</body>
</html>
```